Please look at my website to get a better understanding of my business: www.hearthwell.com
This business is about Life Coaching for Families, couples, teenagers and individuals. I work more w parents of teenagers (as well as teenagers) but not so much with young kids.
The card should be fun, not too busy, with a sense of flow and playfulness. Warm colors, artistic style (can have a family sculpture, paining or a picture in it). Basic information about myself and my company

Reason: I extended my due date for next Tuesday, November 13th. Please summit new designs if you haven't done so, and for those who submitted, thank you so much for your time and effort. I will make a decision next Tues, and will contact you if I need to revise some items. Much thanks to you all! Tali

Families, parents, teenagers, couples, individuals.

Business

• Business name: MoKeRaNu! Kinward Circle Life Coaching
My name: Tali Welbrook, TPLC
Description of my work: Tandem-Path life coach
Tel: 555-304-7129
Website: www.MoKeRaNu.com
• Family sculpture, abstract painting or a picture, or simply a nice background w/out a picture added.
• Corporate feeling, cold colors, corporate symbols. no Sunset, or picture of families on the beach.
Don't include bar-code (from uploaded file 1, it is only the designer to find out more about my website).

```html
<!DOCTYPE html>
<html lang="en">
<head>
<meta charset="utf-8">
<title>Hearthwell business card options</title>
<link rel="stylesheet" href="https://fonts.googleapis.com/css2?family=Fira+Sans:wght@400;700&display=swap">
<style>
  :root {
    --board: #e9eaeb;
    --board-glow: #fbfbfb;
    --mustard: #d19b40;
    --rust: #b95a2a;
    --brick: #b83424;
    --white: #ffffff;
    --ink: #111111;
    --watermark-warm: rgba(214, 120, 60, 0.55);
  }
  html, body {
    margin: 0;
    padding: 0;
    width: 1200px;
    height: 900px;
    overflow: hidden;
  }
  body {
    background: radial-gradient(ellipse at 55% 48%, var(--board-glow) 0%, var(--board) 70%);
    font-family: "Fira Sans", Arial, sans-serif;
    position: relative;
  }
  .option-number {
    position: absolute;
    left: 62px;
    font-weight: 700;
    font-size: 27px;
    color: var(--ink);
  }
  .option-number--one { top: 252px; }
  .option-number--two { top: 598px; }

  .card {
    position: absolute;
    width: 530px;
    height: 298px;
    transform: scale(0.962);
    transform-origin: top left;
    box-shadow: 4px 5px 7px rgba(0, 0, 0, 0.38);
    overflow: hidden;
  }
  .card--mustard { left: 398px; top: 125px; background: var(--mustard); }
  .card--brick { left: 401px; top: 480px; background: var(--brick); }

  .card__bands {
    position: absolute;
    inset: 0;
    width: 530px;
    height: 298px;
  }
  .card__brand {
    position: absolute;
    left: 53px;
    top: 38px;
  }
  .brand-name {
    margin: 0;
    font-weight: 700;
    font-size: 27px;
    line-height: 1;
  }
  .brand-tagline {
    margin: 3px 0 0;
    font-size: 18px;
    line-height: 1.1;
  }
  .card__rule {
    position: absolute;
    left: 0;
    top: 181px;
    width: 69px;
    height: 2px;
    background: var(--white);
  }
  .card__person {
    position: absolute;
    left: 58px;
    top: 176px;
    color: var(--white);
  }
  .person-name {
    margin: 0;
    font-size: 25px;
    line-height: 1.1;
  }
  .person-credential { font-size: 19px; }
  .person-role {
    margin: 1px 0 0;
    font-size: 21px;
    line-height: 1.2;
  }
  .person-phone {
    margin: 13px 0 0;
    font-size: 18px;
  }
  .card--mustard .brand-name,
  .card--mustard .brand-tagline,
  .card--mustard .person-phone { color: var(--rust); }
  .card--brick .brand-name,
  .card--brick .brand-tagline { color: var(--white); }

  .band-watermark {
    font-family: "Fira Sans", Arial, sans-serif;
    font-weight: 700;
    font-size: 70px;
    fill: var(--watermark-warm);
  }
  .band-web {
    font-family: "Fira Sans", Arial, sans-serif;
    font-size: 16px;
  }
</style>
</head>
<body>
  <span class="option-number option-number--one">1</span>
  <span class="option-number option-number--two">2</span>

  <section class="card card--mustard">
    <svg class="card__bands" viewBox="0 0 530 298">
      <polygon points="413,0 530,0 530,30 420,298 295,298" fill="var(--rust)"/>
      <polygon points="530,30 530,298 420,298" fill="var(--brick)"/>
      <text class="band-watermark" x="425" y="165" text-anchor="middle" transform="rotate(-68 425 150)">Hearthwell</text>
      <text class="band-web" x="482" y="208" text-anchor="middle" fill="var(--white)" transform="rotate(-68 482 203)">www.hearthwell.com</text>
    </svg>
    <div class="card__brand">
      <p class="brand-name">Hearthwell</p>
      <p class="brand-tagline">Kinward Circle Life Coaching</p>
    </div>
    <span class="card__rule"></span>
    <div class="card__person">
      <p class="person-name">Tali Welbrook, <span class="person-credential">TPLC</span></p>
      <p class="person-role">Tandem-Path life coach</p>
      <p class="person-phone">Tel: 555-304-7129</p>
    </div>
  </section>

  <section class="card card--brick">
    <svg class="card__bands" viewBox="0 0 530 298">
      <polygon points="413,0 530,0 530,30 420,298 295,298" fill="var(--rust)"/>
      <polygon points="530,30 530,298 420,298" fill="var(--mustard)"/>
      <text class="band-watermark" x="425" y="165" text-anchor="middle" transform="rotate(-68 425 150)">Hearthwell</text>
      <text class="band-web" x="482" y="208" text-anchor="middle" fill="var(--brick)" transform="rotate(-68 482 203)">www.hearthwell.com</text>
    </svg>
    <div class="card__brand">
      <p class="brand-name">Hearthwell</p>
      <p class="brand-tagline">Kinward Circle Life Coaching</p>
    </div>
    <span class="card__rule"></span>
    <div class="card__person">
      <p class="person-name">Tali Welbrook, <span class="person-credential">TPLC</span></p>
      <p class="person-role">Tandem-Path life coach</p>
      <p class="person-phone">Tel: 555-304-7129</p>
    </div>
  </section>
</body>
</html>
```